Business Cards for IT Consulting Company (Managed Service Provider)

I am looking to have some business cards printed and would like some designs. We are an IT Consulting company based in Vancouver BC. I would like a nice clean and modern look to the cards. I have uploaded all the versions of my logo so parts can be used as needed. Here is a snippit from our website homepage:

Kelbrin Systems Ltd. is an IT Solutions Partner located in Vancouver BC, Canada. We offer IT solutions and support to customers in the greater Vancouver Area. With expertise in Quillara platforms, as well as Tovex and Bryn ZPL and over 12 years experience in the IT industry, Kelbrin Systems is dedicated to offering our clients top quality service and products. We take pride in the solutions we offer our customers. The greatest compliment a client can give us is to recommend our services.

Kelbrin Systems Ltd. offers a wide range of IT services from onsite service to remote support and managed service solutions. This allows clients to choose the support path that best suits their company’s needs. Supporting many different sized companies from small to enterprise level over the past 12 years Kelbrin Systems has the experience and expertise needed to ensure things run smoothly. Allowing our clients to focus on doing business.

Revolutionizing the way IT services are delivered.

Kelbrin Systems is dedicated to providing our clients with IT solutions that work and grow with them for years to come. This philosophy helps save money in the long run instead of replacing equipment constantly. Far too often IT solutions are not well thought out and while possibly solving the problem at hand, require replacement due to growth or quality within a very short time frame. Kelbrin Systems takes pride in providing solutions that will last and be able to accommodate growth without the need for replacement.

Industry/Entity Type

Information Technology

Contact Information for Business Card

Kelbrin Systems Ltd.
(Employee Name)
Eml: (Employees Email Address)
Web: kelbrinsys.me
Ph: 604-555-0142

Font styles to use
Serif
Sans Serif

Requirements
Must have
• The Company logo and company colors.
Nice to have
• - Our tag line: "Revolutionizing IT Services" or "Revolutionizing the way IT services are delivered."
• - Also I really like the idea of nature and technology together blending which is sort of where my logo came from so integrating that somehow onto the business cards would be great.

```html
<!DOCTYPE html>
<html lang="en">
<head>
<meta charset="utf-8">
<title>Kelbrin Systems Ltd. — Business Cards</title>
<link href="https://fonts.googleapis.com/css2?family=Montserrat:wght@400;500;600;700;800&display=swap" rel="stylesheet">
<style>
  :root {
    --backdrop: #2b2b2d;
    --card: #050505;
    --brand-blue: #1aa9e8;
    --text-light: #f2f2f2;
    --text-muted: #9a9a9a;
  }
  * { margin: 0; padding: 0; box-sizing: border-box; }
  html, body {
    width: 1200px; height: 900px; overflow: hidden;
    background: var(--backdrop);
    font-family: "Montserrat", sans-serif;
  }
  .canvas { position: relative; width: 1200px; height: 900px; }

  .card {
    position: absolute;
    width: 640px; height: 366px;
    background: var(--card);
    border-radius: 24px;
    overflow: hidden;
    box-shadow: 0 18px 40px rgba(0,0,0,0.55);
  }

  /* Front */
  .card-front { left: 150px; top: 60px; }
  .front-brand {
    position: absolute; left: 0; right: 0; top: 120px;
    display: flex; justify-content: center; align-items: center; gap: 18px;
  }
  .front-brand .brand-square {
    width: 34px; height: 34px; border: 4px solid var(--brand-blue);
  }
  .front-brand .brand-name {
    color: var(--brand-blue); font-weight: 700; font-size: 40px; letter-spacing: 1px;
  }
  .tagline {
    position: absolute; left: 0; right: 0; top: 262px;
    text-align: center; color: var(--text-light);
    font-size: 17px; font-weight: 500; letter-spacing: 1.2px;
  }

  /* Back */
  .card-back { left: 410px; top: 470px; }
  .accent-band {
    position: absolute; right: 0; top: 0; bottom: 0; width: 22px;
    background: var(--brand-blue);
  }
  .back-brand {
    position: absolute; left: 40px; top: 232px;
    display: flex; align-items: center; gap: 12px;
  }
  .back-brand .brand-square {
    width: 22px; height: 22px; border: 3px solid var(--brand-blue);
  }
  .back-brand .brand-name {
    color: var(--brand-blue); font-weight: 700; font-size: 24px; letter-spacing: 0.3px;
  }
  .divider {
    position: absolute; left: 338px; top: 110px; width: 2px; height: 150px;
    background: var(--brand-blue);
  }
  .contact-block { position: absolute; left: 360px; top: 112px; }
  .person-name {
    color: var(--brand-blue); font-weight: 800; font-size: 22px; letter-spacing: 1.5px;
  }
  .person-role {
    color: var(--text-light); font-weight: 600; font-size: 13px; letter-spacing: 1px;
    margin-top: 2px; margin-bottom: 16px;
  }
  .contact-list { list-style: none; }
  .contact-list li {
    display: flex; align-items: center; gap: 10px;
    color: var(--text-light); font-size: 14px; font-weight: 500;
    margin-bottom: 7px; letter-spacing: 0.3px;
  }
  .contact-list svg { width: 12px; height: 12px; flex: none; }
</style>
</head>
<body>
<main class="canvas">

  <section class="card card-front" aria-label="Card front">
    <div class="front-brand">
      <span class="brand-square"></span>
      <span class="brand-name">Kelbrin Systems</span>
    </div>
    <p class="tagline">Revolutionizing IT Services</p>
  </section>

  <section class="card card-back" aria-label="Card back">
    <div class="accent-band"></div>

    <div class="back-brand">
      <span class="brand-square"></span>
      <span class="brand-name">Kelbrin Systems Ltd.</span>
    </div>

    <div class="divider"></div>

    <div class="contact-block">
      <h1 class="person-name">MARLO KESWICK</h1>
      <p class="person-role">DIRECTOR</p>
      <ul class="contact-list">
        <li>
          <svg viewBox="0 0 24 24" fill="var(--brand-blue)"><path d="M6.6 10.8a15.1 15.1 0 0 0 6.6 6.6l2.2-2.2c.3-.3.7-.4 1-.2 1.1.4 2.3.6 3.6.6.6 0 1 .4 1 1V20c0 .6-.4 1-1 1A17 17 0 0 1 3 4c0-.6.4-1 1-1h3.5c.6 0 1 .4 1 1 0 1.3.2 2.5.6 3.6.1.3 0 .7-.2 1z"/></svg>
          604-555-0142
        </li>
        <li>
          <svg viewBox="0 0 24 24" fill="none" stroke="var(--brand-blue)" stroke-width="2.4"><rect x="3" y="5" width="18" height="14" rx="2"/><path d="M3 7l9 6 9-6"/></svg>
          info@marlokeswick.com
        </li>
        <li>
          <svg viewBox="0 0 24 24" fill="none" stroke="var(--brand-blue)" stroke-width="2.2"><circle cx="12" cy="12" r="9"/><path d="M3 12h18M12 3c3 3 3 15 0 18M12 3c-3 3-3 15 0 18"/></svg>
          www.kelbrinsys.me
        </li>
      </ul>
    </div>
  </section>

</main>
</body>
</html>
```